Meadowbrook Fellowship Chapel Banner Design

Designing 6 banners (3 + 3 that will hang on opposite sides of our auditorium) that are 10 feet long by 4 feet wide.

Use our branding guide - specifically item 4 (vertical logo) and item 5 (icon logo).

Design elements found in our AWAKE booklet, we would like to see designs that utilize the white, green and blue colour palettes but NOT the grey. Other colours may be incorporated (e.g. coral).

We are looking for 3 banner designs that would match on either side of the auditorium, the first banner incorporating the word "TRUTH", the second incorporating the word "LOVE", and the third incorporating the word "MISSION".

We interested in incorporating graphics such as trees or outdoor themes.

Font styles to use
Other font styles liked:
• Montserrat

Colors
34a7d7
00a990
f47c35

Requirements
Must have
• Banner Type #1 include the word "TRUTH"
Banner Type #2 include the word "LOVE"
Banner Type #3 include the word "MISSION"

Colour scheme must include CMYK 54 / 5 / 16 / 0 (which is available in the branding guide.) We have selected the three colours, included below in the brief.

From the branding guide - utilize #5 (icon) for the banner.

UPDATE: After reviewing the initial submissions, we are asking for designs that ONLY incorporate #5 - the ICON logo for the banners.
Nice to have
• It would be nice to have some creativity with the colour ... though a more minimalistic style is preferred.

Graphic adaptations such as trees in the background would be of interest.
Should not have
• Colour scheme should not be gray scale.

The banners should NOT be too busy.

Scripture verses (written out) are not necessary.

```html
<!DOCTYPE html>
<html lang="en">
<head>
<meta charset="utf-8">
<title>Meadowbrook Fellowship Chapel — Auditorium Banners</title>
<link rel="stylesheet" href="https://fonts.googleapis.com/css2?family=Montserrat:wght@700&display=swap">
<style>
  :root {
    --truth-blue: #34a7d7;
    --love-green: #00a990;
    --mission-coral: #f47c35;
    --paper: #ffffff;
    --canvas: #fdfdfd;
    --landscape: #525456;
    --banner-w: 263px;
    --banner-h: 657px;
  }
  * { margin: 0; padding: 0; box-sizing: border-box; }
  html, body {
    width: 1200px; height: 933px; overflow: hidden;
    background: var(--canvas);
    font-family: "Montserrat", sans-serif;
  }
  .banner-set { position: relative; width: 1200px; height: 933px; }
  .banner {
    position: absolute; top: 135px;
    width: var(--banner-w); height: var(--banner-h);
    background: var(--tone);
    box-shadow: 2px 3px 5px rgba(0,0,0,0.35);
    overflow: hidden;
  }
  .banner--truth { left: 135px; --tone: var(--truth-blue); }
  .banner--love { left: 475px; --tone: var(--love-green); }
  .banner--mission { left: 815px; --tone: var(--mission-coral); }

  .church-mark {
    position: absolute; left: 50%; top: 41px;
    width: 186px; height: 186px; margin-left: -93px;
    border-radius: 50%;
    border: 4px solid var(--paper);
    display: flex; align-items: center; justify-content: center;
  }
  .church-mark__name {
    font-weight: 700; font-size: 19px; line-height: 1.25;
    text-align: center; color: var(--paper);
  }

  .word-band {
    position: absolute; left: 0; top: 268px; width: 100%; height: 164px;
  }
  .word-band svg { position: absolute; inset: 0; width: 100%; height: 100%; }
  .word-band__word {
    position: absolute; inset: 0;
    display: flex; align-items: center; justify-content: center;
    font-weight: 700; font-size: 50px; letter-spacing: 1px; line-height: 1;
    color: var(--tone);
  }

  .treeline {
    position: absolute; left: 0; bottom: 0; width: 100%; height: 152px;
    background: linear-gradient(to bottom,
      var(--tone) 0%,
      color-mix(in srgb, var(--landscape) 60%, var(--tone)) 30%,
      var(--landscape) 70%,
      var(--landscape) 100%);
  }
</style>
</head>
<body>
<main class="banner-set">
  <section class="banner banner--truth">
    <div class="church-mark">
      <p class="church-mark__name">Meadowbrook<br>Fellowship<br>Chapel</p>
    </div>
    <div class="word-band">
      <svg viewBox="0 0 263 164" preserveAspectRatio="none" aria-hidden="true">
        <path fill="#ffffff" d="M0 14 L8 11 L15 13 L24 9 L33 12 L45 8 L56 11 L66 7 L78 10 L90 8 L101 10 L112 6 L124 9 L137 5 L149 8 L160 6 L172 9 L184 4 L196 8 L208 5 L220 8 L232 6 L244 9 L254 7 L263 9 L263 152 L254 150 L244 155 L232 153 L220 157 L208 154 L196 158 L184 155 L172 159 L160 155 L148 158 L136 154 L124 157 L112 153 L100 157 L88 154 L76 157 L64 153 L52 156 L40 152 L28 156 L16 153 L8 155 L0 153 Z"/>
      </svg>
      <h2 class="word-band__word">TRUTH</h2>
    </div>
    <div class="treeline" role="img" aria-label="Silhouette of a row of trees on a hillside"></div>
  </section>

  <section class="banner banner--love">
    <div class="church-mark">
      <p class="church-mark__name">Meadowbrook<br>Fellowship<br>Chapel</p>
    </div>
    <div class="word-band">
      <svg viewBox="0 0 263 164" preserveAspectRatio="none" aria-hidden="true">
        <path fill="#ffffff" d="M0 14 L8 11 L15 13 L24 9 L33 12 L45 8 L56 11 L66 7 L78 10 L90 8 L101 10 L112 6 L124 9 L137 5 L149 8 L160 6 L172 9 L184 4 L196 8 L208 5 L220 8 L232 6 L244 9 L254 7 L263 9 L263 152 L254 150 L244 155 L232 153 L220 157 L208 154 L196 158 L184 155 L172 159 L160 155 L148 158 L136 154 L124 157 L112 153 L100 157 L88 154 L76 157 L64 153 L52 156 L40 152 L28 156 L16 153 L8 155 L0 153 Z"/>
      </svg>
      <h2 class="word-band__word">LOVE</h2>
    </div>
    <div class="treeline" role="img" aria-label="Silhouette of a row of trees on a hillside"></div>
  </section>

  <section class="banner banner--mission">
    <div class="church-mark">
      <p class="church-mark__name">Meadowbrook<br>Fellowship<br>Chapel</p>
    </div>
    <div class="word-band">
      <svg viewBox="0 0 263 164" preserveAspectRatio="none" aria-hidden="true">
        <path fill="#ffffff" d="M0 14 L8 11 L15 13 L24 9 L33 12 L45 8 L56 11 L66 7 L78 10 L90 8 L101 10 L112 6 L124 9 L137 5 L149 8 L160 6 L172 9 L184 4 L196 8 L208 5 L220 8 L232 6 L244 9 L254 7 L263 9 L263 152 L254 150 L244 155 L232 153 L220 157 L208 154 L196 158 L184 155 L172 159 L160 155 L148 158 L136 154 L124 157 L112 153 L100 157 L88 154 L76 157 L64 153 L52 156 L40 152 L28 156 L16 153 L8 155 L0 153 Z"/>
      </svg>
      <h2 class="word-band__word">MISSION</h2>
    </div>
    <div class="treeline" role="img" aria-label="Silhouette of a row of trees on a hillside"></div>
  </section>
</main>
</body>
</html>
```